Lanternby Consulting Business Card Design

Business Card Design for Lanternby Consulting. Lanternby Consulting is a boutique consultancy based in Atlanta, GA., that specializes in marketing strategy, organization planning, and leadership development. We provide solutions for small businesses and startups as well as Meridex 400 companies.

http://lanternbyconsulting.example/

Target Market(s)

We provide solutions for small businesses and startups as well as Meridex 400 companies.

Industry/Entity Type

Consulting

Contact Information for Business Card

Two sided business card with priority on contact information, logo, tag line (Inspiration to Dream More, Do More, Become More)

Colors

Designer to choose colors to be used in the design.

Requirements
Must have
• contact information, logo, tag line (Inspiration to Dream More, Do More, Become More)
• Simple no over communication.
Nice to have
• I would like to see different placements of logo and creative use of both sides of the card
Should not have
• Do not put too much information on the card.

```html
<!DOCTYPE html>
<html lang="en">
<head>
<meta charset="utf-8">
<title>Lanternby Consulting – Business Card</title>
<link href="https://fonts.googleapis.com/css2?family=Open+Sans:wght@400;600&display=swap" rel="stylesheet">
<style>
  :root {
    --backdrop: #d1d2d4;
    --card: #ffffff;
    --panel-dark: #434343;
    --wave-mid: #a9aaad;
    --wave-light: #e6e6e6;
    --text: #3a3a3a;
    --icon-bg: #7a7a7a;
    --icon-fg: #ffffff;
    --brand: #ffffff;
  }
  * { margin: 0; padding: 0; box-sizing: border-box; }
  html, body {
    width: 1200px; height: 803px; overflow: hidden;
    background: var(--backdrop);
    font-family: "Open Sans", sans-serif;
  }
  .canvas { position: relative; width: 1200px; height: 803px; }
  .card-art { position: absolute; left: 0; top: 0; }
  .brand {
    position: absolute; left: 146px; top: 566px; width: 190px;
    color: var(--brand); font-weight: 600; text-align: center; line-height: 1;
  }
  .brand-name { display: block; font-size: 36px; }
  .brand-sub { display: block; font-size: 14px; letter-spacing: 3px; margin-top: 8px; }
  .contact-list { position: absolute; left: 600px; top: 364px; width: 402px; list-style: none; }
  .contact-item {
    display: flex; align-items: center; justify-content: flex-end;
    height: 42px; margin-bottom: 12.5px;
  }
  .contact-text { font-size: 23px; color: var(--text); letter-spacing: -0.3px; margin-right: 24px; }
  .contact-icon { width: 42px; height: 42px; flex: none; }
</style>
</head>
<body>
<div class="canvas">
  <svg class="card-art" width="1200" height="803" viewBox="0 0 1200 803">
    <defs>
      <clipPath id="card-shape"><rect x="104" y="118" width="992" height="568" rx="48"/></clipPath>
      <linearGradient id="wave-mid-fill" x1="0" y1="0" x2="0" y2="1">
        <stop offset="0" stop-color="#f2f2f2"/>
        <stop offset="0.45" stop-color="#c9c9cb"/>
        <stop offset="1" stop-color="var(--wave-mid)"/>
      </linearGradient>
      <linearGradient id="wave-light-fill" x1="0" y1="0" x2="0" y2="1">
        <stop offset="0" stop-color="#ffffff"/>
        <stop offset="1" stop-color="var(--wave-light)"/>
      </linearGradient>
    </defs>
    <rect class="card" x="104" y="118" width="992" height="568" rx="48" fill="var(--card)"/>
    <g clip-path="url(#card-shape)">
      <path class="wave-light" fill="url(#wave-light-fill)"
        d="M308,118 C250,185 244,280 298,380 C330,440 352,475 384,512 C436,572 480,625 504,686 H104 V118 Z"/>
      <path class="wave-mid" fill="url(#wave-mid-fill)"
        d="M300,118 C244,190 246,285 292,372 C322,430 350,470 380,508 C424,566 458,624 472,686 H104 V118 Z"/>
      <path class="panel-dark" fill="var(--panel-dark)"
        d="M104,118 H258 C244,160 222,240 232,320 C240,372 300,440 352,484 C380,530 370,600 344,686 H104 Z"/>
    </g>
  </svg>

  <div class="brand">
    <span class="brand-name">Lanternby</span>
    <span class="brand-sub">CONSULTING</span>
  </div>

  <ul class="contact-list">
    <li class="contact-item">
      <span class="contact-text">Add location</span>
      <svg class="contact-icon" viewBox="0 0 42 42" aria-hidden="true">
        <circle cx="21" cy="21" r="21" fill="var(--icon-bg)"/>
        <path d="M21 11 a7 7 0 0 1 7 7 c0 5 -7 13 -7 13 s-7 -8 -7 -13 a7 7 0 0 1 7 -7 z" fill="var(--icon-fg)"/>
        <circle cx="21" cy="18" r="2.6" fill="var(--icon-bg)"/>
      </svg>
    </li>
    <li class="contact-item">
      <span class="contact-text">lanternbyconsulting.example</span>
      <svg class="contact-icon" viewBox="0 0 42 42" aria-hidden="true">
        <circle cx="21" cy="21" r="21" fill="var(--icon-bg)"/>
        <g fill="none" stroke="var(--icon-fg)" stroke-width="1.8">
          <circle cx="21" cy="21" r="10"/>
          <ellipse cx="21" cy="21" rx="4.5" ry="10"/>
          <line x1="11" y1="21" x2="31" y2="21"/>
          <line x1="13" y1="16" x2="29" y2="16"/>
          <line x1="13" y1="26" x2="29" y2="26"/>
        </g>
      </svg>
    </li>
    <li class="contact-item">
      <span class="contact-text">add mail</span>
      <svg class="contact-icon" viewBox="0 0 42 42" aria-hidden="true">
        <circle cx="21" cy="21" r="21" fill="var(--icon-bg)"/>
        <g fill="none" stroke="var(--icon-fg)" stroke-width="1.8" stroke-linejoin="round">
          <rect x="10" y="14" width="22" height="15"/>
          <path d="M10 14 L21 23 L32 14"/>
          <path d="M10 29 L18 21 M32 29 L24 21"/>
        </g>
      </svg>
    </li>
    <li class="contact-item">
      <span class="contact-text">Add Phone</span>
      <svg class="contact-icon" viewBox="0 0 42 42" aria-hidden="true">
        <circle cx="21" cy="21" r="21" fill="var(--icon-bg)"/>
        <path d="M15 11 l4 0 l2 6 l-3 2 c1.5 3 3.5 5 6 6 l2 -3 l6 2 l0 4 c0 1.5 -1.5 2.5 -3 2.5 c-9 -1 -15 -7 -16 -16 c0 -1.5 1 -3.5 2 -3.5 z" fill="var(--icon-fg)"/>
      </svg>
    </li>
  </ul>
</div>
</body>
</html>
```